3D Scans and Virtual Tour photography company needs a website

We need a website build that explains what we do, shows some examples of our 3d scans and virtual tours, some stats on why they are important when when selling your home or marketing your business/premises and a contact form to find out more. We need to target both the real estate agents and consumers. The site needs to looks modern, engaging, clean, not lots of text but more pictures and icons. Needs to be mobile friendly. In fact i would build it from the mobile then out.

Reason: Hi Team, I have had a couple of requests to extend the Project deadline, which I have now done. I cant push it much more than this as the business is up and running now and I need the website. Looking forward to reviewing the designs.

Target Market(s)

people selling their home and the real estate industry mostly, however any building can be scanned and have a 3d tour

Industry/Entity Type

Photographer

Font styles to use
Sans Serif

Colors
32a6d6
0355a3
33a6d7
85cae6
cee9f5
3176b5

Requirements
Must have
• Our logo
• an example of the 3d scans
• an example of a dollhouse view
• a contact page
• Replace the orange document examples to blue please
• social media links Facebook Instagram Twitter
Nice to have
• some examples of similar companies websites we like
• favourite would be this one brindlenook (dot com)
• next fav roomvale (dot com au) and wexlorn (dot com au)

```html
<!DOCTYPE html>
<html lang="en">
<head>
<meta charset="utf-8">
<title>Brightfold Imagery – 3D Tours</title>
<link href="https://fonts.googleapis.com/css2?family=Open+Sans:wght@400;600;700;800&display=swap" rel="stylesheet">
<style>
:root{
  --sky:#32a6d6;
  --navy:#0355a3;
  --mid:#3176b5;
  --pale:#85cae6;
  --mist:#cee9f5;
  --ink:#222;
  --text:#555;
  --band:#e8e8e8;
  --foot:#ececec;
  --white:#fff;
  --accent:#d9363e;
  --line:#dcdcdc;
}
*{box-sizing:border-box;margin:0;padding:0}
html,body{width:1200px;height:5114px;overflow:hidden}
body{font-family:"Open Sans",Arial,sans-serif;color:var(--text);background:var(--white);position:relative}
section,header,nav,footer{position:relative;width:1200px;overflow:hidden}
svg{display:block}

/* header */
.site-header{height:102px;background:var(--white)}
.brand{position:absolute;left:62px;top:30px;display:flex;align-items:center;gap:12px;font-size:30px;font-weight:700;color:var(--navy)}
.brand-dot{width:22px;height:22px;border-radius:50%;background:var(--sky)}
.call-box{position:absolute;right:0;top:0;width:317px;height:96px;background:var(--mid);color:var(--white);padding:14px 0 0 30px;display:flex;gap:16px}
.call-icon{width:44px;height:44px;border-radius:50%;border:2px solid var(--white);display:flex;align-items:center;justify-content:center;margin-top:6px}
.call-text small{display:block;font-size:14px}
.call-text strong{display:block;font-size:26px;font-weight:700;line-height:1.1}
.call-text span{font-size:13px}

.main-nav{height:28px;background:var(--mist);display:flex;align-items:center;gap:38px;padding-left:56px;border-bottom:2px solid var(--pale)}
.main-nav a{font-size:14px;font-weight:600;color:var(--mid);text-decoration:none;text-transform:uppercase}

/* hero */
.hero{height:596px}
.hero-media{position:absolute;inset:0;background:linear-gradient(180deg,#4d90c0 0%,#8fc2de 45%,#c7dfe8 62%,#6f9a4a 72%,#4f7a30 100%)}
.hero-title{position:absolute;left:66px;top:60px;width:520px;font-size:40px;font-weight:600;line-height:1.18;color:var(--white)}

/* process */
.process{height:484px;background:linear-gradient(180deg,#fff 0%,#eaf6fb 100%)}
.section-rule{position:absolute;top:58px;left:0;width:1200px;display:flex;align-items:center;justify-content:center;gap:26px;font-size:22px;font-weight:700;color:var(--ink)}
.section-rule::before,.section-rule::after{content:"";width:320px;height:2px;background:#333}
.step{position:absolute;top:110px;width:260px;text-align:center}
.step-ring{width:160px;height:160px;margin:0 auto;border-radius:50%;background:var(--mist);display:flex;align-items:center;justify-content:center}
.step-core{width:132px;height:132px;border-radius:50%;background:var(--white);border:5px solid var(--sky);display:flex;align-items:center;justify-content:center}
.step-pill{display:inline-block;margin-top:28px;padding:5px 34px;background:var(--sky);color:var(--white);font-weight:700;font-size:18px;border-radius:18px}
.step-text{margin-top:14px;font-size:16px;font-weight:600;color:#333;line-height:1.3}
.step-text em{font-style:normal;color:var(--sky)}
.link-line{position:absolute;top:190px;height:3px;background:var(--pale)}
.link-label{position:absolute;top:160px;font-size:17px;font-weight:600;color:var(--sky);text-align:center}

/* features */
.features{height:460px;background:var(--white)}
.features h2{position:absolute;left:62px;top:65px;font-size:22px;font-weight:700;color:var(--ink)}
.feature-list{position:absolute;left:70px;top:120px;list-style:none;width:330px}
.feature-list li{display:flex;gap:18px;margin-bottom:16px;font-size:15px;line-height:1.35;color:#444}
.feature-list svg{flex:none}
.plan-media{position:absolute;left:572px;top:52px;width:316px;height:290px;background:linear-gradient(135deg,#f2ece2,#b99e7c 60%,#8b6a4a);transform:skewY(-8deg);border-radius:6px}
.try{position:absolute;left:930px;top:110px;width:230px;text-align:center}
.try h3{font-size:24px;font-weight:700;color:var(--mid)}
.try p{margin-top:8px;font-size:14px;color:#444;line-height:1.4}
.btn{display:inline-block;background:var(--mid);color:var(--white);font-weight:700;border-radius:22px;text-decoration:none}
.try .btn{margin-top:30px;padding:12px 42px;font-size:16px}

/* devices */
.showcase{height:682px;background:linear-gradient(180deg,#3a3a3a,#262626)}
.showcase h2{position:absolute;top:60px;width:100%;text-align:center;color:var(--white);font-size:24px;font-weight:700}
.device{position:absolute;background:#f4f4f4;box-shadow:0 10px 24px rgba(0,0,0,.45)}
.device .screen{position:absolute;background:var(--white);overflow:hidden}
.available{position:absolute;top:560px;width:100%;text-align:center;color:var(--sky);font-size:15px;font-weight:700}
.badge{position:absolute;top:590px;height:40px;background:#555;border-radius:4px}

/* mock listing page inside a screen */
.mock-bar{height:9%;background:var(--white);border-bottom:1px solid var(--line);display:flex;align-items:center;gap:6%;padding:0 5%}
.mock-bar i{display:block;height:30%;background:var(--line);flex:1}
.mock-bar i:first-child{background:var(--accent);flex:.6}
.mock-body{display:flex;gap:4%;padding:4%;height:91%}
.mock-main{flex:3;display:flex;flex-direction:column;gap:6%}
.mock-side{flex:1;display:flex;flex-direction:column;gap:6%}
.mock-photo{flex:4;border-radius:2px}
.mock-lines{flex:1;background:repeating-linear-gradient(180deg,var(--line) 0 5px,transparent 5px 12px)}
.mock-thumb{flex:1;background:#e6e1d8}
.tone-plan{background:linear-gradient(135deg,#efe6d6,#a9825c 55%,#6d4e35)}
.tone-room{background:linear-gradient(160deg,#f3f1ec,#c9c0b0 55%,#8f8676)}
.tone-house{background:linear-gradient(135deg,#e8edf0,#c7b296 50%,#8a6b4f)}
.tone-street{background:linear-gradient(180deg,#dfe8ee,#b7c0a4 60%,#72845a)}

/* stand out */
.standout{height:460px}
.standout h2{position:absolute;left:66px;top:60px;font-size:32px;font-weight:700;color:var(--ink)}
.tablet{position:absolute;width:358px;height:269px;background:linear-gradient(180deg,#1c1c1c,#3b3b3b);border-radius:22px;padding:22px}
.tablet .screen{width:100%;height:100%;background:var(--white);overflow:hidden}
.view-card{position:absolute;width:420px}
.view-card h3{display:flex;align-items:flex-end;gap:16px;font-size:24px;font-weight:400;color:var(--ink)}
.view-card h3 b{color:var(--sky);font-weight:400}
.view-card p{margin-top:16px;font-size:15px;color:#444}

.stat-band{height:62px;background:var(--band);text-align:center;padding-top:9px}
.stat-band h4{font-size:19px;font-weight:400;color:var(--sky)}
.stat-band p{font-size:14px;color:#333}

.view{height:364px}

/* benefits */
.benefits{height:808px;background:var(--white)}
.benefit{position:absolute;width:300px;text-align:center}
.benefit svg{margin:0 auto}
.benefit h5{margin-top:18px;font-size:20px;font-weight:400;color:#333}
.benefit p{margin:14px auto 0;width:260px;font-size:14px;line-height:1.45;color:#555}

/* cta */
.cta{height:232px;display:flex}
.cta-media{width:600px;height:232px;background:linear-gradient(90deg,#9fb0bd,#e9eef1 70%)}
.cta-panel{width:600px;background:var(--mid);color:var(--white);text-align:center;padding-top:50px}
.cta-panel h2{font-size:24px;font-weight:700}
.cta-panel strong{display:block;font-size:52px;font-weight:700;line-height:1.1}
.cta-panel span{font-size:18px}

.newsletter{height:75px;background:#3a3a3a;color:var(--white)}
.newsletter h3{position:absolute;left:66px;top:22px;font-size:24px;font-weight:700}
.newsletter p{position:absolute;left:528px;top:14px;width:420px;font-size:14px;line-height:1.4}
.newsletter .btn{position:absolute;left:964px;top:20px;padding:7px 20px;font-size:16px;background:var(--mid);display:flex;gap:12px;align-items:center}

/* footer */
.site-footer{height:229px;background:var(--foot);font-size:14px;color:#333}
.site-footer h6{font-size:16px;font-weight:700;color:#222;margin-bottom:6px}
.foot-links{position:absolute;left:68px;top:20px;line-height:1.4}
.foot-contact{position:absolute;left:256px;top:20px;line-height:1.4}
.social{display:flex;gap:10px;margin:10px 0 8px}
.social i{width:16px;height:16px;border-radius:50%;background:#555}
.message{position:absolute;left:522px;top:20px}
.field{position:absolute;background:var(--white);border:1px solid #ccc;color:#888;padding:6px 10px;font-size:14px}
.submit{position:absolute;background:var(--mid);color:var(--white);font-weight:700;text-align:center;padding-top:4px}
.copyright{height:44px;background:var(--white);padding:16px 0 0 66px;font-size:13px;color:#555}
</style>
</head>
<body>

<header class="site-header">
  <div class="brand"><span class="brand-dot"></span>Brightfold Imagery</div>
  <div class="call-box">
    <div class="call-icon">
      <svg width="22" height="22" viewBox="0 0 24 24"><path d="M6 2l4 4-2 3c1.5 3 4 5.5 7 7l3-2 4 4-3 4C10 21 3 14 2 5z" fill="#fff"/></svg>
    </div>
    <div class="call-text"><small>Call us</small><strong>1800 555 019</strong><span>hello@brightfoldmedia.com.au</span></div>
  </div>
</header>

<nav class="main-nav">
  <a>Home</a><a>3D Camera</a><a>3D Tours</a><a>Industries</a><a>Virtual Reality</a><a>Support</a><a>Blog</a><a>Contact</a>
</nav>

<section class="hero">
  <div class="hero-media" role="img" aria-label="Hand holding a tablet with a wireframe house rising from a patch of grass under a blue sky"></div>
  <h1 class="hero-title">Transform your business<br>through the power of<br>immersive media</h1>
</section>

<section class="process">
  <h2 class="section-rule">Brightfold Imagery Process</h2>
  <div class="link-line" style="left:330px;width:175px"></div>
  <div class="link-label" style="left:380px;width:80px">2 hrs</div>
  <div class="link-line" style="left:668px;width:175px"></div>
  <div class="link-label" style="left:715px;width:80px">48 hrs</div>

  <div class="step" style="left:119px">
    <div class="step-ring"><div class="step-core">
      <svg width="60" height="60" viewBox="0 0 60 60" fill="none" stroke="#32a6d6" stroke-width="4"><rect x="6" y="16" width="48" height="34" rx="5"/><path d="M20 16l4-7h12l4 7"/><circle cx="30" cy="33" r="10"/></svg>
    </div></div>
    <span class="step-pill">SCAN</span>
    <p class="step-text">Capture a space<br>in <em>3D</em></p>
  </div>
  <div class="step" style="left:456px">
    <div class="step-ring"><div class="step-core">
      <svg width="64" height="56" viewBox="0 0 64 56" fill="none" stroke="#32a6d6" stroke-width="4"><path d="M16 44a12 12 0 0 1 0-24 16 16 0 0 1 31-3 12 12 0 0 1 2 27z"/><path d="M32 48V26M24 33l8-8 8 8"/></svg>
    </div></div>
    <span class="step-pill">UPLOAD</span>
    <p class="step-text">Process &amp; store in<br>the <em>cloud</em></p>
  </div>
  <div class="step" style="left:797px">
    <div class="step-ring"><div class="step-core">
      <svg width="40" height="62" viewBox="0 0 40 62" fill="none" stroke="#32a6d6" stroke-width="4"><rect x="3" y="3" width="34" height="56" rx="5"/><path d="M3 12h34M3 48h34"/><circle cx="20" cy="54" r="1.5"/></svg>
    </div></div>
    <span class="step-pill">VIEW</span>
    <p class="step-text">Experience via<br><em>web &amp; mobile</em></p>
  </div>
</section>

<section class="features">
  <h2>Complementary Features</h2>
  <ul class="feature-list">
    <li><svg width="24" height="28" viewBox="0 0 24 28" fill="none" stroke="#3176b5" stroke-width="2"><rect x="2" y="2" width="20" height="24"/><path d="M6 9h12M6 14h12M6 19h8"/></svg>1. 3D Tour (integrated into Homeport and Nestlist)</li>
    <li><svg width="24" height="28" viewBox="0 0 24 28" fill="none" stroke="#3176b5" stroke-width="2"><rect x="2" y="2" width="20" height="24"/><path d="M2 12h10v14M12 12V2"/></svg>2. Traditional Floor Plan (With Measurements)</li>
    <li><svg width="24" height="28" viewBox="0 0 24 28" fill="none" stroke="#3176b5" stroke-width="2"><rect x="2" y="2" width="20" height="24"/><circle cx="12" cy="12" r="5"/></svg>3. Company branding and digital presence</li>
    <li><svg width="24" height="28" viewBox="0 0 24 28" fill="none" stroke="#3176b5" stroke-width="2"><rect x="2" y="2" width="20" height="24"/><path d="M6 22v-6M12 22V9M18 22v-9"/></svg>4. Fortnightly analytic reports</li>
    <li><svg width="24" height="28" viewBox="0 0 24 28" fill="none" stroke="#3176b5" stroke-width="2"><rect x="2" y="2" width="20" height="24"/><path d="M6 14l4 4 8-9"/></svg>5. Leading web integration and backend support</li>
  </ul>
  <div class="plan-media" role="img" aria-label="Furnished 3D floor plan of an apartment seen from above"></div>
  <div class="try">
    <h3>Try it for yourself</h3>
    <p>Hit the Start 3D button to experience our feature tour</p>
    <a class="btn">START 3D</a>
  </div>
</section>

<section class="showcase">
  <h2>Stop Buyers In Their Tracks With An Engaging 3D Tour.</h2>

  <div class="device" style="left:300px;top:120px;width:620px;height:380px;border-radius:10px">
    <div class="screen" style="left:14px;top:14px;right:14px;bottom:14px">
      <div class="mock-bar"><i></i><i></i><i></i><i></i><i></i></div>
      <div class="mock-body">
        <div class="mock-main">
          <div class="mock-photo tone-room" role="img" aria-label="Listing page with a living room walkthrough photo"></div>
          <div class="mock-lines"></div>
        </div>
        <div class="mock-side"><div class="mock-thumb"></div><div class="mock-thumb"></div><div class="mock-thumb"></div></div>
      </div>
    </div>
  </div>

  <div class="device" style="left:110px;top:210px;width:300px;height:320px;border-radius:18px">
    <div class="screen" style="left:16px;top:26px;right:16px;bottom:26px">
      <div class="mock-bar"><i></i><i></i><i></i></div>
      <div class="mock-body">
        <div class="mock-main">
          <div class="mock-photo tone-street" role="img" aria-label="Listing page showing a house exterior"></div>
          <div class="mock-lines"></div>
        </div>
      </div>
    </div>
  </div>

  <div class="device" style="left:900px;top:200px;width:120px;height:300px;border-radius:18px">
    <div class="screen" style="left:8px;top:34px;right:8px;bottom:34px">
      <div class="mock-bar"><i></i><i></i></div>
      <div class="mock-body" style="flex-direction:column">
        <div class="mock-photo tone-house" style="flex:2" role="img" aria-label="Mobile listing with property photo"></div>
        <div class="mock-lines"></div>
      </div>
    </div>
  </div>

  <p class="available">Available On</p>
  <div class="badge" style="left:430px;width:175px"></div>
  <div class="badge" style="left:635px;width:125px"></div>
</section>

<section class="standout">
  <h2>Stand Out Online By Attracting The Right Buyers.</h2>
  <div class="tablet" style="left:143px;top:147px"><div class="screen">
    <div class="mock-bar"><i></i><i></i><i></i><i></i></div>
    <div class="mock-body">
      <div class="mock-main"><div class="mock-photo tone-plan" role="img" aria-label="Live floor plan of a listing seen from above"></div><div class="mock-lines"></div></div>
      <div class="mock-side"><div class="mock-thumb"></div><div class="mock-thumb"></div></div>
    </div>
  </div></div>
  <div class="view-card" style="left:620px;top:220px">
    <h3><svg width="50" height="50" viewBox="0 0 50 50" fill="none" stroke="#32a6d6" stroke-width="3"><path d="M4 4h42v42H4zM4 26h18v20M22 4v12M30 26h16"/></svg><span>Live <b>Floor</b> Plan</span></h3>
    <p>Examine the property from above.</p>
  </div>
</section>

<section class="stat-band"><h4>Buyers Love 3D Tours!</h4><p>80% increase in enquiries for properties with 3D Tours</p></section>

<section class="view">
  <div class="view-card" style="left:68px;top:126px">
    <h3><svg width="50" height="50" viewBox="0 0 50 50" fill="none" stroke="#32a6d6" stroke-width="3"><path d="M25 4l20 10v22L25 46 5 36V14zM5 14l20 10 20-10M25 24v22"/></svg><span>3D <b>Dollhouse</b> View</span></h3>
    <p>View the property in three dimensions</p>
  </div>
  <div class="tablet" style="left:699px;top:41px"><div class="screen">
    <div class="mock-bar"><i></i><i></i><i></i><i></i></div>
    <div class="mock-body">
      <div class="mock-main"><div class="mock-photo tone-house" role="img" aria-label="3D dollhouse view of a two storey home"></div><div class="mock-lines"></div></div>
      <div class="mock-side"><div class="mock-thumb"></div><div class="mock-thumb"></div></div>
    </div>
  </div></div>
</section>

<section class="stat-band"><h4>Online Engagement</h4><p>Users spend 52% longer on listings featuring 3D Tours</p></section>

<section class="view">
  <div class="tablet" style="left:143px;top:51px"><div class="screen">
    <div class="mock-bar"><i></i><i></i><i></i><i></i></div>
    <div class="mock-body">
      <div class="mock-main"><div class="mock-photo tone-room" role="img" aria-label="First person walkthrough of a living room"></div><div class="mock-lines"></div></div>
      <div class="mock-side"><div class="mock-thumb"></div><div class="mock-thumb"></div></div>
    </div>
  </div></div>
  <div class="view-card" style="left:630px;top:125px">
    <h3><svg width="50" height="50" viewBox="0 0 50 50" fill="none" stroke="#32a6d6" stroke-width="3"><path d="M4 4h42v42H4z"/><circle cx="25" cy="14" r="4" fill="#32a6d6"/><path d="M25 20v12l-6 10M25 32l6 10M18 26h14"/></svg><span>First <b>Person</b> View</span></h3>
    <p>Experience the property as if you were physically there</p>
  </div>
</section>

<section class="stat-band"><h4>Better Than Video</h4><p>3D Tours provide 4x engagement compared to video</p></section>

<section class="benefits">
  <div class="benefit" style="left:89px;top:100px">
    <svg width="70" height="70" viewBox="0 0 70 70" fill="none" stroke="#3176b5" stroke-width="3"><path d="M8 34L35 10l27 24M16 28v32h38V28M29 60V42h12v18"/></svg>
    <h5>Integration</h5>
    <p>With the 3D Tour integration across online real estate portals, the property will stand out instantly from the search results with the bold 3D icon. Click here to see what it looks like</p>
  </div>
  <div class="benefit" style="left:450px;top:100px">
    <svg width="70" height="70" viewBox="0 0 70 70" fill="none" stroke="#3176b5" stroke-width="3"><path d="M20 62V48c-8-5-12-13-10-22 3-13 18-20 30-15 9 4 13 12 12 20l6 10h-7v9H40v12"/><circle cx="33" cy="30" r="8"/></svg>
    <h5>Connect</h5>
    <p>A 3D Tour allows for genuine buyers to build an emotional connection with the property</p>
  </div>
  <div class="benefit" style="left:811px;top:100px">
    <svg width="70" height="70" viewBox="0 0 70 70" fill="none" stroke="#3176b5" stroke-width="3"><circle cx="35" cy="35" r="27"/><path d="M35 18v17l11 7"/></svg>
    <h5>Time</h5>
    <p>Buyers spend an additional 3.4 minutes engaged in a listing with a 3D Tour compared to those without</p>
  </div>
  <div class="benefit" style="left:89px;top:458px">
    <svg width="70" height="70" viewBox="0 0 70 70"><circle cx="35" cy="35" r="28" fill="#3176b5"/><path d="M20 22c6 2 10 0 14 5-2 6-8 5-9 12-1 5-6 6-9 2M40 14c3 5 10 6 12 12-4 3-7 1-10 5s2 10-3 14" fill="none" stroke="#fff" stroke-width="3"/></svg>
    <h5>Share</h5>
    <p>3D Tours allow for increasive interaction with the property for remote and overseas buyers</p>
  </div>
  <div class="benefit" style="left:450px;top:458px">
    <svg width="70" height="70" viewBox="0 0 70 70" fill="none" stroke="#3176b5" stroke-width="5"><path d="M35 6v58M48 20c-3-5-9-6-14-6-7 0-12 4-12 10 0 14 27 8 27 22 0 7-6 10-13 10-6 0-12-2-15-7"/></svg>
    <h5>Value</h5>
    <p>Perceived value of the property increases as a direct result of sophisticated marketing</p>
  </div>
  <div class="benefit" style="left:811px;top:458px">
    <svg width="70" height="70" viewBox="0 0 70 70" fill="#3176b5"><rect x="8" y="44" width="10" height="18"/><rect x="24" y="34" width="10" height="28"/><rect x="40" y="24" width="10" height="38"/><rect x="56" y="12" width="10" height="50"/><path d="M6 36L30 18l12 6 18-16" fill="none" stroke="#32a6d6" stroke-width="3"/></svg>
    <h5>Analytics</h5>
    <p>Detailed analytics allows assessment of traffic to 3D Tours in real time</p>
  </div>
</section>

<section class="cta">
  <div class="cta-media" role="img" aria-label="Person wearing a virtual reality headset against a pale background"></div>
  <div class="cta-panel">
    <h2>Book Your 3D Tour Today!</h2>
    <strong>1800 555 019</strong>
    <span>hello@brightfoldmedia.com.au</span>
  </div>
</section>

<section class="newsletter">
  <h3>Sign Up Our Newsletter!</h3>
  <p>Sign up today for our newsletter and receive latest news and also get our tips &amp; exclusive offers.</p>
  <a class="btn">SIGN UP <svg width="22" height="22" viewBox="0 0 22 22"><circle cx="11" cy="11" r="10" fill="#fff"/><path d="M9 6l5 5-5 5" fill="none" stroke="#3176b5" stroke-width="2.5"/></svg></a>
</section>

<footer class="site-footer">
  <div class="foot-links">
    <h6>Quick Links</h6>
    3D Camera<br>3D Tours<br>Industries<br>Virtual Reality<br>Support<br>Blog<br>Contact
  </div>
  <div class="foot-contact">
    <h6>Brightfold Imagery</h6>
    48 Harbour Lane Suite 12<br>Newtown, NS 2042
    <div class="social"><i></i><i></i><i></i></div>
    T: 1800 555 019<br>E: hello@brightfoldmedia.com.au
  </div>
  <div class="message"><h6>Leave A Message</h6></div>
  <div class="field" style="left:522px;top:52px;width:245px;height:36px">Name</div>
  <div class="field" style="left:522px;top:100px;width:245px;height:36px">Email</div>
  <div class="field" style="left:522px;top:148px;width:245px;height:36px">Phone</div>
  <div class="field" style="left:777px;top:52px;width:348px;height:132px">Message</div>
  <div class="submit" style="left:777px;top:190px;width:348px;height:32px">SUBMIT</div>
</footer>

<div class="copyright">©2017 Brightfold Imagery. All rights reserved</div>

</body>
</html>
```